Foster/Adoptive Family Ministry needs a postcard design to highlight changed lives

Kin Harbor is a non profit that finds and supports foster and adoptive families for kids in need. We need a postcard design that features families and children who have experienced a changed life by working with Kin Harbor. I'm thinking of a postcard that is custom size...so that it fits in a #10 envelope. So that 3 cards could be printed on an 8 1/2 x 11 card stock. The card should be front and back with a layout for a couple of photos, our logo, a headline and some text that will tell the story of the family. This is all about telling a story. The primary audience for the card is donors, and prospective donors. I don't have photos or the text yet, so I'm looking for an editable layout where I can drop text and photos in.

Industry/Entity Type

Non Profit

```html
<!DOCTYPE html>
<html lang="en">
<head>
<meta charset="utf-8">
<title>Kin Harbor Postcard</title>
<link rel="stylesheet" href="https://fonts.googleapis.com/css2?family=Arimo:wght@400;700&family=PT+Sans+Narrow:wght@400;700&family=Open+Sans:wght@400;600&family=Roboto+Condensed:wght@400;700&display=swap">
<style>
  :root {
    --brand-blue: #2f62c8;
    --poem-blue: #2a5cc4;
    --headline-red: #c4121a;
    --heart-pink: #ee4468;
    --url-salmon: #f4918a;
    --ink: #1a1a1a;
    --paper: #ffffff;
    --backdrop: #ece2d2;
  }
  * { box-sizing: border-box; margin: 0; padding: 0; }
  html, body { width: 1200px; height: 1200px; overflow: hidden; background: var(--backdrop); }
  .card { position: absolute; left: 68px; width: 1065px; height: 533px; background: var(--paper); overflow: hidden; }
  .card--front { top: 42px; }
  .card--back { top: 620px; }
  .front-art { position: absolute; inset: 0; }

  .headline-box {
    position: absolute; left: 318px; top: 0; width: 268px; height: 148px;
    background: var(--headline-red); color: #fff;
    font-family: 'Arimo', Arial, sans-serif; font-weight: 700;
    font-size: 56px; line-height: 52px; text-align: center; padding-top: 24px;
  }
  .poem {
    position: absolute; left: 40px; top: 38px; width: 225px;
    font-family: 'PT Sans Narrow', 'Arial Narrow', sans-serif;
    color: var(--poem-blue); font-size: 20px; line-height: 22.3px; text-align: center;
  }
  .brand-name {
    position: absolute; font-family: 'Open Sans', Arial, sans-serif; font-weight: 600;
    color: #1f2b44; font-size: 38px; letter-spacing: -0.5px; white-space: nowrap;
    display: flex; align-items: center; gap: 10px;
  }
  .brand-name .dot { width: 14px; height: 14px; border-radius: 50%; background: var(--brand-blue); }
  .card--front .brand-name { left: 12px; top: 445px; }

  .contact { position: absolute; left: 302px; top: 416px; color: #fff; }
  .contact .phone {
    font-family: 'Arimo', Arial, sans-serif; font-weight: 700; font-size: 29px;
    display: flex; align-items: center; gap: 6px;
  }
  .contact .email { font-family: 'PT Sans Narrow', sans-serif; font-weight: 700; font-size: 29px; margin-top: 2px; }
  .contact .tax { font-family: 'Roboto Condensed', sans-serif; font-size: 16px; margin-top: 2px; }
  .tagline {
    position: absolute; right: 40px; top: 438px; color: #fff; text-align: right;
    font-family: 'Arimo', Arial, sans-serif; font-variant: small-caps; font-size: 33px;
    letter-spacing: 2.5px; line-height: 34px;
  }

  .back-copy { position: absolute; left: 35px; top: 12px; width: 450px; }
  .back-copy h1 {
    font-family: 'Arimo', Arial, sans-serif; font-weight: 700; color: var(--heart-pink);
    font-size: 38px; letter-spacing: 3px;
  }
  .back-copy h2 {
    font-family: 'Arimo', Arial, sans-serif; font-weight: 700; color: var(--poem-blue);
    font-size: 22.5px; letter-spacing: 2.2px; line-height: 24px; margin-top: 2px;
  }
  .back-copy p {
    font-family: 'Open Sans', Arial, sans-serif; color: var(--ink);
    font-size: 17px; line-height: 22.2px; margin-top: 6px; letter-spacing: -0.2px;
  }
  .card--back .brand-name { left: 125px; top: 458px; }
  .divider { position: absolute; left: 510px; top: 0; width: 3px; height: 420px; background: var(--url-salmon); }
  .back-photo {
    position: absolute; left: 514px; top: 0; width: 551px; height: 420px;
    background: linear-gradient(100deg, #3f6a2c 0%, #5d8a3e 35%, #7a6a48 60%, #b98564 80%, #8c6a4a 100%);
  }
  .action-band {
    position: absolute; left: 509px; top: 420px; width: 556px; height: 113px;
    background: var(--brand-blue); text-align: center; padding-top: 6px;
    font-family: 'Roboto Condensed', Arial, sans-serif;
  }
  .action-band .call { color: #fff; font-weight: 700; font-size: 24px; line-height: 27px; }
  .action-band .url { color: var(--url-salmon); font-weight: 700; font-size: 32px; margin-top: 6px; }
</style>
</head>
<body>
  <section class="card card--front">
    <svg class="front-art" width="1065" height="533" viewBox="0 0 1065 533">
      <defs>
        <linearGradient id="meadow" x1="0" y1="0" x2="0" y2="1">
          <stop offset="0" stop-color="#7f9a6a"/>
          <stop offset="0.45" stop-color="#6f9447"/>
          <stop offset="1" stop-color="#55782f"/>
        </linearGradient>
      </defs>
      <rect x="270" y="0" width="795" height="440" fill="url(#meadow)" role="img" aria-label="Photo of a smiling family with young children standing in a summer meadow"/>
      <polygon points="0,0 305,0 268,533 0,533" fill="#fff"/>
      <polygon points="0,0 37,0 12,533 0,533" fill="var(--brand-blue)"/>
      <path d="M268,388 Q560,418 760,424 Q940,428 1065,408 L1065,533 L268,533 Z" fill="var(--brand-blue)"/>
    </svg>

    <div class="headline-box">The Gift<br>of Life</div>

    <div class="poem">
      I didn’t give you<br>the gift of life,<br>But in my heart<br>i know,<br>The love I feel is<br>deep and real,<br>As if it had been so,<br>For us to have<br>each other<br>is like a dream<br>come true!<br>No, I didn’t give you<br>The gift of life,<br>Life gave me<br>the gift of you.
    </div>

    <div class="brand-name"><span class="dot"></span>Kin Harbor</div>

    <div class="contact">
      <div class="phone">
        <svg width="24" height="24" viewBox="0 0 24 24"><circle cx="12" cy="12" r="10" fill="none" stroke="#fff" stroke-width="2"/><path d="M9 7 Q7 12 10 17 L12 16 L11 13 L10 13 Q9.5 11 10 10 L11 10 L12 7 Z" fill="#fff"/></svg>
        406.555.0182
      </div>
      <div class="email">info@kinharbormontana.org</div>
      <div class="tax">Tax exempt, 501(c)3, Public Charity #27-5519048</div>
    </div>

    <div class="tagline">A Forever Family<br>For Every Child</div>
  </section>

  <section class="card card--back">
    <div class="back-copy">
      <h1>Open your heart.</h1>
      <h2>Become a foster or adoptive parent to one of the over 2,000 children in Montana in need of a loving home.</h2>
      <p>Kin Harbor has a two pronged approach: Recruiting and Support. Bridging the gap between churches, communities and government, Kin Harbor builds awareness and recruits foster and adoptive families for Montana children via churches across the state. Additionally, working closely with pastors and congregations, they work to support those families caring for children from “hard places” by utilizing the natural infrastructure of the church. Additional educational, therapeutic and family support resources and referrals to other child welfare leaders are also provided.</p>
    </div>

    <div class="brand-name"><span class="dot"></span>Kin Harbor</div>

    <div class="divider"></div>
    <div class="back-photo" role="img" aria-label="Photo of a mother tenderly holding a young boy close, with green foliage behind them"></div>

    <div class="action-band">
      <div class="call">HELP NOW!<br>You can make a difference!</div>
      <div class="url">kinharbormontana.org</div>
    </div>
  </section>
</body>
</html>
```